Water Filter Company Needs Bizz Cards!!

Need business cards for my company. We sell whole home water filters and salt free water softeners. No more buying bottled water. Our filtering units filter out all heavy metals, chlorine, and VOC's, last 15 years, and are maintenance free and supply your whole home with spring quality alkaline water. Our Salt free water conditioners, eliminate hard water and scale, without lowering the ph, or TDS's (total Dissolved solids)

I think this is the color code we are using on my site. My logo looks good behind it. #192841

Website will be www.Brovexa.com

Industry/Entity Type

Water Purification

Contact Information for Business Card

For now, just insert standard Dummy text. I need these text lines for the info to be editable so i can make them for multiple employees. I do have Photoshop and illustrator, unless there is a simpler program i can use solely for biz cards

Font styles to use
Sans Serif

Requirements
Must have
• Use my preexisting logo.

www.BroVexa.com

Spring Quality Alkaline Water at every tap.

List out services. Whole Home Water Filters, Salt Free Water Softeners, Clarimont KT7, UV Sterilizers
Nice to have
• I think this is the color code we are using on my site. My logo looks good behind it. #192841 or black. Please no white or light blue backgrounds.

Maybe a picture of my tank.

Slogan like Spring Quality Alkaline Water at every tap.
And just list the services Whole Home Water Filters, Salt Free Water Softeners, Clarimont KT7, UV Sterilizers

I think I would like to not have a contrasting textured logo like I see on some of them. I may use it for my personal cards, but new employees may not want the extra expense.
Should not have
• A different logo than the one provided.

White or baby blue backgrounds. Use the color code, or blacks.

```html
<!DOCTYPE html>
<html lang="en">
<head>
<meta charset="utf-8">
<title>Brovexa – Business Card</title>
<link rel="stylesheet" href="https://fonts.googleapis.com/css2?family=Lato:wght@700;900&family=Roboto:wght@400;500&display=swap">
<style>
  :root {
    --page-bg: #e6e4e4;
    --card-charcoal: #1b1b1d;
    --card-navy: #192841;
    --accent-sky: #38bfee;
    --disc-light: #f2eeee;
    --disc-warm: #e6d3d4;
    --ink-dark: #3b3b3b;
    --ink-white: #ffffff;
  }
  * { margin: 0; padding: 0; box-sizing: border-box; }
  html, body {
    width: 1200px;
    height: 900px;
    overflow: hidden;
    background: var(--page-bg);
  }
  .business-card {
    position: absolute;
    left: 100px;
    top: 141px;
    width: 1000px;
    height: 618px;
    background: var(--card-navy);
    overflow: hidden;
    box-shadow: 0 10px 30px rgba(0,0,0,0.15);
  }
  .charcoal-band {
    position: absolute;
    left: 0; top: 0;
    width: 300px; height: 100%;
    background: var(--card-charcoal);
  }
  .brand-disc {
    position: absolute;
    left: 34px; top: 43px;
    width: 532px; height: 532px;
    border-radius: 50%;
    background: radial-gradient(circle at 40% 40%, var(--disc-light) 0%, #ece4e5 60%, var(--disc-warm) 100%);
  }
  .brand-name {
    position: absolute;
    left: 0; width: 100%;
    top: 180px;
    text-align: center;
    font-family: "Lato", sans-serif;
    font-weight: 900;
    font-size: 82px;
    letter-spacing: -1px;
    color: var(--ink-dark);
  }
  .brand-slogan {
    position: absolute;
    left: 0; width: 100%;
    top: 325px;
    text-align: center;
    font-family: "Roboto", sans-serif;
    font-size: 28px;
    line-height: 36px;
    color: var(--ink-dark);
  }
  .contact-panel {
    position: absolute;
    left: 601px;
    top: 92px;
    width: 370px;
    color: var(--ink-white);
    font-family: "Roboto", sans-serif;
  }
  .person-name {
    font-family: "Lato", sans-serif;
    font-weight: 900;
    font-size: 38px;
    line-height: 40px;
    letter-spacing: -0.5px;
  }
  .person-role {
    font-size: 28px;
    line-height: 30px;
  }
  .contact-list {
    list-style: none;
    margin-top: 28px;
    font-size: 28px;
    line-height: 36.5px;
  }
  .contact-list li {
    display: flex;
    align-items: center;
    gap: 9px;
  }
  .contact-icon {
    width: 26px; height: 26px;
    flex: none;
  }
  .postal-address {
    margin-top: 24px;
    font-style: normal;
    font-size: 28px;
    line-height: 36px;
  }
  .service-list {
    list-style: none;
    margin-top: 24px;
    padding-top: 16px;
    border-top: 2px solid var(--accent-sky);
    font-size: 20px;
    line-height: 27px;
  }
  .service-list li {
    display: flex;
    align-items: center;
    gap: 10px;
  }
  .service-list li::before {
    content: "";
    width: 8px; height: 8px;
    border-radius: 50%;
    background: var(--accent-sky);
    flex: none;
  }
</style>
</head>
<body>
  <article class="business-card">
    <div class="charcoal-band"></div>

    <div class="brand-disc">
      <div class="brand-name">Brovexa</div>
      <p class="brand-slogan">Spring Quality Alkaline<br>Water at every tap</p>
    </div>

    <section class="contact-panel">
      <h1 class="person-name">DANIEL HARPER</h1>
      <p class="person-role">Managing Director</p>

      <ul class="contact-list">
        <li>
          <svg class="contact-icon" viewBox="0 0 24 24" aria-hidden="true">
            <path fill="#fff" d="M6.6 10.8c1.4 2.8 3.8 5.1 6.6 6.6l2.2-2.2c.3-.3.7-.4 1-.2 1.1.4 2.3.6 3.6.6.6 0 1 .4 1 1V20c0 .6-.4 1-1 1C10.6 21 3 13.4 3 4c0-.6.4-1 1-1h3.5c.6 0 1 .4 1 1 0 1.3.2 2.5.6 3.6.1.3 0 .7-.2 1L6.6 10.8z"/>
          </svg>
          84 0900 555 014
        </li>
        <li>
          <svg class="contact-icon" viewBox="0 0 24 24" aria-hidden="true">
            <rect x="2" y="5" width="20" height="14" fill="#fff"/>
            <path d="M2 5l10 8 10-8" fill="none" stroke="#192841" stroke-width="1.6"/>
          </svg>
          info@brovexa.com
        </li>
        <li>
          <svg class="contact-icon" viewBox="0 0 24 24" aria-hidden="true">
            <g fill="none" stroke="#fff" stroke-width="1.6">
              <circle cx="12" cy="12" r="9.5"/>
              <ellipse cx="12" cy="12" rx="4.2" ry="9.5"/>
              <path d="M2.5 12h19M4 7h16M4 17h16"/>
            </g>
          </svg>
          www.BroVexa.com
        </li>
      </ul>

      <address class="postal-address">
        214 Hoa Sen Street<br>
        Tay Ho, Ha Noi
      </address>

      <ul class="service-list">
        <li>Whole Home Water Filters</li>
        <li>Salt Free Water Softeners</li>
        <li>Clarimont KT7</li>
        <li>UV Sterilizers</li>
      </ul>
    </section>
  </article>
</body>
</html>
```